It is a leisure sector investment company.The company plans to invest in a luxurious 5 star resort

We need a stationery design to our company 'Copper Lantern Limited' using the winning logo design. We need the letter heads, envelopes & the business cards. Should be simple, plain and professional
We have upload the source file & vector files which gives our logo design. We prefer the bottom logo.

Have updated under 'must have priorities', the company name, address, tel no. fax no. & the company reg no. which should come on the letter head. the long envelope should have the company name, tel & fax no. 
Business card should have the company name, name on the card, designation, tel no. fax no.  

- Letter head details:
Copper Lantern Limited
14 Floor, South Wing, Halvard Merchant Plaza,
Merrow Court, Colombo 01, Sri Lanka
Tel: +94 11 5047293 Fax: +94 11 5047298
Company Reg No.QX 6142
Long Envelope should have only the company name, adress, Tel & Fax
Business Cards should have the company name, Tel & Fax:
Business Card 1 - Lasantha Gunaratne - Chairman
Business Card 2 - Nimal.T.Wijesooriya - COO

```html
<!DOCTYPE html>
<html lang="en">
<head>
<meta charset="utf-8">
<title>Copper Lantern Limited – Business Card</title>
<link rel="stylesheet" href="https://fonts.googleapis.com/css2?family=Cinzel:wght@400&family=Tinos&display=swap">
<style>
  :root {
    --paper: #ffffff;
    --card: #a39565;
    --card-pattern: #ab9e70;
    --ink: #463c31;
    --label: #111111;
  }
  * { margin: 0; padding: 0; box-sizing: border-box; }
  html, body {
    width: 1200px;
    height: 394px;
    overflow: hidden;
    background: var(--paper);
  }
  .sheet {
    position: relative;
    width: 1200px;
    height: 394px;
  }
  .side-label {
    position: absolute;
    top: 2px;
    font-family: "Tinos", "Times New Roman", serif;
    font-size: 21px;
    color: var(--label);
    letter-spacing: 0.5px;
  }
  .side-label--front { left: 3px; }
  .side-label--back { left: 638px; }

  .card {
    position: absolute;
    top: 49px;
    width: 571px;
    height: 345px;
    background: var(--card);
    overflow: hidden;
  }
  .card--front { left: 0; }
  .card--back { left: 629px; }

  .card__pattern {
    position: absolute;
    inset: 0;
    background: radial-gradient(ellipse at center, var(--card) 40%, var(--card-pattern) 100%);
  }

  .brand {
    position: absolute;
    left: 0;
    right: 0;
    top: 160px;
    text-align: center;
    font-family: "Cinzel", "Trajan Pro", serif;
    font-weight: 400;
    color: var(--ink);
  }
  .brand__name {
    display: block;
    font-size: 46px;
    line-height: 1;
    letter-spacing: 1px;
  }
  .brand__suffix {
    display: block;
    margin-top: 10px;
    font-size: 30px;
    line-height: 1;
    letter-spacing: 10px;
    padding-left: 10px;
  }

  .contact {
    position: absolute;
    left: 0;
    right: 0;
    text-align: center;
    font-family: "Tinos", "Times New Roman", serif;
    color: var(--ink);
  }
  .contact__holder {
    top: 122px;
    font-size: 20px;
  }
  .contact__address {
    top: 163px;
    font-size: 11.5px;
  }
  .contact__phones {
    top: 194px;
    font-size: 11.5px;
    word-spacing: 1px;
  }
</style>
</head>
<body>
  <main class="sheet">
    <span class="side-label side-label--front">FRONT</span>
    <span class="side-label side-label--back">BACK</span>

    <section class="card card--front">
      <div class="card__pattern" role="img" aria-label="Faint tone-on-tone damask scroll pattern across the card"></div>
      <h1 class="brand">
        <span class="brand__name">COPPER LANTERN</span>
        <span class="brand__suffix">LIMITED</span>
      </h1>
    </section>

    <section class="card card--back">
      <p class="contact contact__holder">Lasantha Gunaratne - Chairman</p>
      <p class="contact contact__address">14, floor, South Wing, Halvard Merchant Plaza, Merrow Court, Colombo 01, Sri Lanka</p>
      <p class="contact contact__phones">Tel No. &nbsp;+94 11 5047293 &nbsp;Fax No. &nbsp;+94 11 5047298</p>
    </section>
  </main>
</body>
</html>
```